Brochure Design Project for Brockwell and Daughter Lumber

We are after an executive high-end trifold brochure to be sent to new customers. Please refer to document attached ('brochure notes') for the details.

Target Market(s)

Renovators, Wives, Architects, Builders

Requirements
Must have
• Back of brochure must have a map and contact details.

Must relate to the feel of our website ... brockwellanddaughterlumber.net

Nice to have
• A unique design - something unlike regular brochures.

Developed using Adobe Photoshop or InDesign

```html
<!DOCTYPE html>
<html lang="en">
<head>
<meta charset="utf-8">
<title>Brockwell and Daughter Lumber – Trifold Brochure</title>
<link href="https://fonts.googleapis.com/css2?family=Arvo:wght@700&family=Cabin:wght@400;600;700&family=Caveat:wght@600&display=swap" rel="stylesheet">
<style>
  :root{
    --cream:#ece8df;
    --cream-light:#f1ede5;
    --charcoal:#45423a;
    --taupe:#7a7166;
    --heading-grey:#7a766b;
    --text:#2e2b26;
    --beige:#bfb69d;
    --green:#84c341;
    --green-panel:#a0cd5c;
    --map:#e6e3db;
    --white:#ffffff;
  }
  *{box-sizing:border-box;margin:0;padding:0}
  html,body{width:1200px;height:848px;overflow:hidden;background:var(--cream)}
  body{font-family:"Cabin",Arial,sans-serif;color:var(--text)}
  .brochure{position:relative;width:1200px;height:848px;background:var(--cream)}
  .abs{position:absolute}
  .photo{position:absolute;border-radius:20px;overflow:hidden}

  /* left panel */
  .section-title{left:0;top:28px;width:388px;height:72px;background:var(--charcoal);
    color:var(--white);font-family:"Arvo",Georgia,serif;font-size:23px;line-height:28px;padding:7px 13px}
  .intro{left:24px;top:116px;width:325px;font-size:17px;line-height:20px}
  .intro strong{font-size:22px;font-weight:700}
  .accent-bar-beige{left:363px;top:123px;width:25px;height:343px;background:var(--beige)}
  .timber-photo{left:24px;top:216px;width:339px;height:250px;
    background:linear-gradient(160deg,#5b4a3a 0%,#8a6a48 45%,#b07a44 100%)}
  .photo-caption{right:32px;bottom:14px;color:var(--white);font-size:15px;font-weight:600;line-height:18px}
  .accent-bar-green{left:24px;top:487px;width:24px;height:341px;background:var(--green)}
  .bamboo-text{left:61px;top:484px;width:327px;font-size:17px;line-height:20.5px}
  .bamboo-text strong{font-size:22px}
  .bamboo-photo-room{left:48px;top:621px;width:196px;height:207px;border-radius:20px 20px 0 20px;
    background:linear-gradient(180deg,#6c6259 0%,#c9b48e 60%,#b89a62 100%)}
  .bamboo-photo-detail{left:259px;top:621px;width:129px;height:207px;border-radius:20px 0 0 20px;
    background:linear-gradient(160deg,#c7b59c 0%,#9e7443 50%,#7c5430 100%)}

  /* middle panel */
  .cash-tag{left:412px;top:34px;width:142px;height:142px}
  .star-heading{left:565px;top:34px;font-size:26px;line-height:27px;font-weight:600;color:var(--heading-grey)}
  .star-text{left:565px;top:90px;width:232px;font-size:15.5px;line-height:18px}
  .services-heading{left:411px;top:207px;font-size:26px;font-weight:600;color:var(--heading-grey)}
  .services{left:411px;top:240px;display:flex;font-size:16px;line-height:19px}
  .services li{list-style:none;padding:0 7px;border-left:1px solid var(--text)}
  .services li:first-child{padding-left:0;border-left:none}
  .contact-panel{left:399px;top:309px;width:400px;height:265px;background:var(--green-panel);
    border-radius:0 24px 24px 0;color:var(--white)}
  .panel-brand{position:absolute;left:28px;top:28px;display:flex;align-items:center;gap:12px;
    font-size:26px;font-weight:700;line-height:30px;width:350px}
  .brand-dot{width:58px;height:58px;border-radius:50%;background:var(--white);flex:none}
  .contact-list{position:absolute;left:13px;top:146px;width:380px;font-size:16px;line-height:27px;color:var(--text)}
  .contact-list dt{float:left;clear:left;width:70px;color:var(--white);font-size:17px}
  .contact-list dd{margin-left:70px;white-space:nowrap}
  .map{left:520px;top:591px;width:268px;height:181px;
    background:linear-gradient(90deg,rgba(230,227,219,0) 0%,var(--map) 35%,var(--map) 100%);z-index:0}
  .visit-title{left:411px;top:606px;font-family:"Caveat",cursive;font-size:27px;color:var(--text);z-index:1}
  .visit-address{left:411px;top:639px;font-size:16px;line-height:20px;z-index:1}
  .hours{left:411px;top:713px;font-size:14.5px;line-height:18px;z-index:1}
  .hours strong{font-size:16px;font-weight:600}
  .web-bar{left:399px;top:793px;width:400px;height:35px;background:var(--charcoal);color:var(--white);
    font-size:15px;line-height:35px;padding-left:13px}
  .web-bar span{font-size:18px}

  /* right panel */
  .cover{left:799px;top:0;width:401px;height:848px;background:var(--taupe)}
  .cover-brand{left:885px;top:0;width:226px;height:244px;background:var(--cream-light);
    display:flex;flex-direction:column;align-items:center;justify-content:center;gap:14px;
    color:var(--taupe);font-size:24px;font-weight:700;text-align:center;line-height:28px;padding:0 14px}
  .cover-brand .brand-dot{background:var(--taupe);width:70px;height:70px}
  .tagline{left:812px;top:252px;width:380px;text-align:center;font-family:"Caveat",cursive;
    font-size:40px;color:var(--cream-light)}
  .framed{border:4px solid var(--cream-light);border-radius:16px}
  .deck-pool{left:815px;top:320px;width:371px;height:257px;
    background:linear-gradient(135deg,#2d6fa3 0%,#8fb6c9 30%,#a07462 55%,#8a5f4d 100%)}
  .deck-dining{left:815px;top:596px;width:371px;height:236px;
    background:linear-gradient(160deg,#b8b3a8 0%,#6e5135 45%,#4e3522 100%)}
</style>
</head>
<body>
<main class="brochure">

  <!-- Inner left panel -->
  <h1 class="abs section-title">Traditional Timber<br>and Bamboo Flooring</h1>
  <p class="abs intro"><strong>Timber flooring</strong> is a natural, environmentally friendly option that can add real value to your home.<br>Come and see our showroom today!</p>
  <div class="abs accent-bar-beige"></div>
  <div class="photo timber-photo" role="img" aria-label="Kitchen with warm timber floorboards">
    <p class="abs photo-caption">Timber flooring<br>photo tag here</p>
  </div>
  <div class="abs accent-bar-green"></div>
  <p class="abs bamboo-text"><strong>Bamboo flooring</strong> is an increasingly popular choice for many homeowners, architects, builders and interior designers who are looking for an environmental alternative to timber flooring that is a stylish, hard wearing, pre-finished flooring system.</p>
  <div class="photo bamboo-photo-room" role="img" aria-label="Living room with white sofas on bamboo flooring"></div>
  <div class="photo bamboo-photo-detail" role="img" aria-label="Close-up of bamboo floorboards with cushion and decor"></div>

  <!-- Middle panel -->
  <svg class="abs cash-tag" viewBox="0 0 142 142" role="img" aria-label="Gold tag reading Want Cash?">
    <defs>
      <radialGradient id="goldFill" cx="40%" cy="35%" r="70%">
        <stop offset="0" stop-color="#f6d769"/>
        <stop offset="1" stop-color="#c9931a"/>
      </radialGradient>
    </defs>
    <circle cx="71" cy="71" r="66" fill="url(#goldFill)"/>
    <circle cx="71" cy="71" r="58" fill="none" stroke="#fff3c2" stroke-width="1.5"/>
    <text x="71" y="70" text-anchor="middle" font-family="Arvo, serif" font-weight="700" font-size="28" fill="#fff">Want</text>
    <text x="71" y="102" text-anchor="middle" font-family="Arvo, serif" font-weight="700" font-size="28" fill="#fff">Cash?</text>
  </svg>
  <h2 class="abs star-heading">Become a<br>renovation star!</h2>
  <p class="abs star-text">If you allow us to take photos, video or leave a sign, we will reward you with $50 cash for every order taken from interest in your home improvement.</p>
  <h2 class="abs services-heading">Other services in our offer:</h2>
  <ul class="abs services">
    <li>We can come to you for<br>free measure and quote.</li>
    <li>Design<br>advise</li>
    <li>We can organize<br>full installation.</li>
  </ul>

  <section class="abs contact-panel">
    <div class="panel-brand"><span class="brand-dot"></span><span>Brockwell and Daughter Lumber</span></div>
    <dl class="contact-list">
      <dt>Call Us</dt><dd>1300 555 018, (07) 5550 1234</dd>
      <dt>Fax</dt><dd>(07) 5550 7890</dd>
      <dt>Email</dt><dd>info@brockwellanddaughterlumber.com.au</dd>
      <dt>Post</dt><dd>PO Box 1187, Harbourview BC 4220</dd>
    </dl>
  </section>

  <div class="abs map" role="img" aria-label="Street map showing the showroom location"></div>
  <h3 class="abs visit-title">Come See Us</h3>
  <p class="abs visit-address">Unit 7 / 42 Marlow Road<br>Ashgrove Plains 4118,<br>Queensland, Australia</p>
  <p class="abs hours"><strong>Open hours</strong><br>Monday-Friday<br>10.30-17.30</p>
  <p class="abs web-bar">Visit our website: <span>brockwellanddaughterlumber.net</span></p>

  <!-- Cover panel -->
  <section class="abs cover"></section>
  <div class="abs cover-brand"><span class="brand-dot"></span><span>Brockwell and Daughter Lumber</span></div>
  <p class="abs tagline">Building better lifestyles</p>
  <div class="photo framed deck-pool" role="img" aria-label="Timber deck beside a pool overlooking the water"></div>
  <div class="photo framed deck-dining" role="img" aria-label="Outdoor dining table on a dark timber deck"></div>

</main>
</body>
</html>
```